Tab-Fix Notes
3inx3in Tab Fix Notes with "Thank You!" message
Tab-Fix Notes - Corporate Services
Creative Brief
In need of designs for 3inch x 3inch Tab Fix Notes. Company Branding and Image (professional, high energy, uplifting, splash of color) The words "Thank You" and company website (www.marlowbrekke.com) must be included on actual tab fix.
Corporate Services
Corporate and professional, but modern.
3inch by 3 inch tab fix size. Use your creativity to the fullest but handwritten notes must legible on tab-fix. White backgrounds are okay as long as message stands out. Color preference of background - hot pink, orange, neon blue, neon green The words "Thank You" and company website (www.marlowbrekke.com) must be included on actual tab fix.
Related Contests
Social Media Banner Design (for Chatterloop, Zanvio+, Peepwire, and WorkNexa) based on current website.
Concepts
The Beacon Planning Institute Banner Display

```html
<!DOCTYPE html>
<html lang="en">
<head>
<meta charset="UTF-8">
<title>Tab-Fix Notes – Thank You</title>
<link rel="stylesheet" href="https://fonts.googleapis.com/css2?family=Great+Vibes&family=Open+Sans:wght@400&display=swap">
<style>
  :root {
    --page-bg: #ffffff;
    --note-bg: #f6f6f6;
    --rule: #1a1a1a;
    --band-red: #e2120f;
    --band-deep: #c80d0a;
    --band-glow: #ff7a1a;
    --brand-red: #e8301a;
    --text-light: #ffffff;
  }
  html, body {
    margin: 0;
    padding: 0;
    width: 1200px;
    height: 871px;
    overflow: hidden;
    background: var(--page-bg);
  }
  .canvas {
    position: relative;
    width: 1200px;
    height: 871px;
  }
  .note {
    position: absolute;
    left: 341px;
    top: 111px;
    width: 588px;
    height: 666px;
    background: var(--note-bg);
    box-shadow: 0 0 0 1px #efefef;
    overflow: hidden;
  }
  .brand-name {
    position: absolute;
    right: 24px;
    top: 30px;
    margin: 0;
    font-family: "Great Vibes", cursive;
    font-size: 34px;
    font-weight: 400;
    color: var(--brand-red);
    line-height: 1;
  }
  .footer-rule {
    position: absolute;
    left: 0;
    right: 0;
    top: 531px;
    height: 5px;
    background: var(--rule);
  }
  .footer-band {
    position: absolute;
    left: 0;
    right: 0;
    top: 541px;
    bottom: 0;
    background:
      radial-gradient(ellipse 110px 70px at 386px 58px, var(--band-glow) 0%, rgba(255,122,26,0.45) 40%, rgba(226,18,15,0) 100%),
      linear-gradient(180deg, var(--band-red), var(--band-deep));
  }
  .thank-you {
    position: absolute;
    left: 0;
    right: 0;
    top: 14px;
    margin: 0;
    text-align: center;
    padding-left: 60px;
    font-family: "Great Vibes", cursive;
    font-weight: 400;
    font-size: 70px;
    line-height: 1;
    color: var(--text-light);
  }
  .website {
    position: absolute;
    right: 12px;
    bottom: 10px;
    margin: 0;
    font-family: "Open Sans", Arial, sans-serif;
    font-size: 16px;
    color: var(--text-light);
  }
</style>
</head>
<body>
  <main class="canvas">
    <section class="note">
      <p class="brand-name">Marlow Brekke</p>
      <div class="footer-rule"></div>
      <footer class="footer-band">
        <h1 class="thank-you">Thank You!</h1>
        <p class="website">www.marlowbrekke.com</p>
      </footer>
    </section>
  </main>
</body>
</html>
```